Notary Signing Agent Need Business card Design

Need a Business card design for my new company. RT Velo-Brisk LLC
Mobile Notary Signing Agent. I go to the customer for closing of Mortgage's Documents . possible signs of honesty, integrity and confidentiality.

Work with Title company to Notary Mortgage closing.

My Target Market is Title companies. Banks and Financial Institution.

Color Blue to Black Professional ) if needed some Green Little Red

And possible a company logo.

Mobile ( travel to clients ) Integrity, Honest Trustworthy. A show of Professional services.

Would like company name and my name on card

Use both sides and front with business name and my name. phone numbers.

Target Market(s)

Title company, Banks mortgage company

Industry/Entity Type

Travel

Contact Information for Business Card

Notary, Certified signing agent, Mobile

Colors
0455a3

Requirements
Must have
• Name of company , owners name phone number,
Nice to have
• blue and black color like a professional look but not limit to these only.
• a stand out from other cards .

```html
<!DOCTYPE html>
<html lang="en">
<head>
<meta charset="utf-8">
<title>RT Velo-Brisk LLC — Business Card</title>
<link rel="stylesheet" href="https://fonts.googleapis.com/css2?family=Roboto+Condensed:wght@700&family=Montserrat:wght@300;400&display=swap">
<style>
  :root {
    --brand-blue: #0455a3;
    --blue-deep: #034a8f;
    --charcoal: #3b3b3d;
    --charcoal-dark: #2f2f31;
    --charcoal-light: #454547;
    --text-white: #f2f2f2;
    --text-muted: #b9bcc2;
    --page-bg: #e7e8ea;
  }
  * { margin: 0; padding: 0; box-sizing: border-box; }
  html, body { width: 1200px; height: 1000px; overflow: hidden; }
  body { background: var(--page-bg); position: relative; }
  .card {
    position: absolute;
    width: 525px;
    height: 300px;
    box-shadow: 0 10px 28px rgba(0,0,0,0.22);
  }
  .card svg { display: block; width: 100%; height: 100%; }
  .card-front { left: 120px; top: 150px; }
  .card-back { left: 555px; top: 550px; }
  .company-name { font-family: "Roboto Condensed", "Arial Narrow", sans-serif; font-weight: 700; fill: var(--text-white); }
  .company-suffix { font-family: "Montserrat", sans-serif; font-weight: 300; fill: var(--text-muted); }
  .contact-text { font-family: "Montserrat", sans-serif; font-weight: 400; fill: var(--text-white); }
  .person-name { font-family: "Montserrat", sans-serif; font-weight: 400; fill: var(--text-white); letter-spacing: 1.5px; }
  .icon-letter { font-family: "Montserrat", sans-serif; font-weight: 400; fill: var(--brand-blue); }
</style>
</head>
<body>

<section class="card card-front" aria-label="Business card front">
  <svg viewBox="0 0 525 300" xmlns="http://www.w3.org/2000/svg">
    <rect class="front-field" width="525" height="300" fill="var(--brand-blue)"/>
    <polygon class="front-top-corner" points="0,0 525,0 525,62 420,18 0,18" fill="var(--charcoal)"/>
    <polygon class="front-contact-band" points="0,262 200,248 525,226 525,300 0,300" fill="var(--charcoal)"/>
    <polygon class="front-corner-stripe" points="0,262 200,248 150,256 0,272" fill="var(--blue-deep)"/>
    <polygon class="front-bottom-corner" points="0,272 150,256 200,300 0,300" fill="var(--charcoal-dark)"/>

    <text class="company-title" x="272" y="150" text-anchor="middle">
      <tspan class="company-name" font-size="48">RT Velo-Brisk</tspan><tspan class="company-suffix" font-size="30" dx="10">LLC</tspan>
    </text>

    <g class="contact-row" transform="translate(150,275)">
      <polygon points="0,-8 7,-4 7,4 0,8 -7,4 -7,-4" fill="var(--text-white)"/>
      <text class="icon-letter" x="0" y="4" font-size="10" text-anchor="middle">P</text>
      <text class="contact-text" x="12" y="5" font-size="14">555-214-3307</text>
      <polygon points="125,-8 132,-4 132,4 125,8 118,4 118,-4" fill="var(--text-white)"/>
      <text class="icon-letter" x="125" y="4" font-size="10" text-anchor="middle">F</text>
      <text class="contact-text" x="137" y="5" font-size="14">555-386-9142</text>
      <circle cx="245" cy="0" r="3" fill="var(--text-white)"/>
      <text class="contact-text" x="253" y="5" font-size="13">Daniel R Hollis</text>
    </g>
  </svg>
</section>

<section class="card card-back" aria-label="Business card back">
  <svg viewBox="0 0 525 300" xmlns="http://www.w3.org/2000/svg">
    <rect class="back-field" width="525" height="300" fill="var(--charcoal)"/>
    <polygon class="back-notch" points="90,0 240,0 300,178 140,98" fill="var(--charcoal-light)"/>
    <polygon class="back-panel" points="240,0 525,0 525,212 300,178" fill="var(--brand-blue)"/>
    <polygon class="back-stripe" points="40,115 140,98 525,212 525,232" fill="var(--brand-blue)"/>

    <text class="person-name" x="395" y="75" font-size="15" text-anchor="middle">Daniel R Hollis</text>

    <g class="contact-phone" transform="translate(340,132)">
      <polygon points="0,-8 7,-4 7,4 0,8 -7,4 -7,-4" fill="var(--text-white)"/>
      <path d="M-3,-3 q0,6 6,6 l1,-2 -2,-1 -1,1 q-2,-1 -3,-3 l1,-1 -1,-2 z" fill="var(--brand-blue)"/>
      <text class="contact-text" x="13" y="5" font-size="14">555-214-3307</text>
    </g>
    <g class="contact-office" transform="translate(360,160)">
      <polygon points="0,-8 7,-4 7,4 0,8 -7,4 -7,-4" fill="var(--text-white)"/>
      <rect x="-3" y="-3" width="6" height="6" fill="var(--brand-blue)"/>
      <text class="contact-text" x="13" y="5" font-size="14">555-386-9142</text>
    </g>

    <text class="company-title" x="30" y="272">
      <tspan class="company-name" font-size="40">RT Velo-Brisk</tspan><tspan class="company-suffix" font-size="26" dx="10">LLC</tspan>
    </text>
  </svg>
</section>

</body>
</html>
```